Business Card Design

Electric home brewing equipment. Custom and catalog items. Most products are made by or for my company, so name is on most everything. Travel to conventions, to meet with home brewers. Trying to create a professional, but since primarily home brewers, fun image. New logo attached, with this new logo I'm redoing most materials. I'm trying to create a single brand under this logo.
Bolt icon on card, does not have to be directly over text as in logo file, but can be used similar to my example.

Website address is http://www.voltkettleworks.com (this is a must add).

New video intro to be added to video productions here: http://clipvault.example/k7Rm2xQwLp

Target Market(s)

Home brewers, predominantly male, ages 21 - 55, tend to be looking for the hot new thing.

Industry/Entity Type

Business

Contact Information for Business Card

Details as included on file. Layout I've attached is approximately what I'm looking for. Single and Double sided cards options welcome.

Card info should include:
2 cards: Derek Holm and Mona Holm
Both: Owners
Email: derek@voltkettleworks.com and mona@voltkettleworks.com
Both phone: 888-472-0635
Both address: Lakeview, Texas 77512
Website: voltkettleworks.com

Requirements
Must have
• Use both parts of the logo, not necessarily together as design should infer.

```html
<!DOCTYPE html>
<html lang="en">
<head>
<meta charset="UTF-8">
<title>Volt Kettle Works — Business Cards</title>
<link rel="stylesheet" href="https://fonts.googleapis.com/css2?family=Montserrat:wght@500;800&family=Lato:wght@400;700&display=swap">
<style>
  :root {
    --backdrop: #3a3431;
    --card-black: #161616;
    --card-white: #ffffff;
    --ink: #151515;
    --volt-yellow: #f7b718;
    --ring-grey: #4a4a4a;
  }
  * { margin: 0; padding: 0; box-sizing: border-box; }
  html, body { width: 1200px; height: 716px; overflow: hidden; }
  body {
    background: var(--backdrop);
    font-family: "Lato", Arial, sans-serif;
    position: relative;
  }
  .card {
    position: absolute;
    width: 500px;
    height: 286px;
    overflow: hidden;
    border-radius: 4px;
    box-shadow: 0 10px 30px rgba(0,0,0,.35);
  }
  .card-back { left: 60px; top: 56px; background: var(--card-black); }
  .card-front.derek { left: 640px; top: 56px; }
  .card-front.mona { left: 350px; top: 374px; }

  /* Back side */
  .card-back .brand-mark {
    position: absolute;
    left: 50%; top: 50%;
    transform: translate(-50%, -50%);
    display: flex; flex-direction: column; align-items: center; gap: 16px;
  }
  .card-back .brand-circle {
    width: 70px; height: 70px;
    border: 9px solid var(--ring-grey);
    border-radius: 50%;
  }
  .card-back .brand-name {
    font-family: "Montserrat", Arial, sans-serif;
    font-weight: 800;
    font-size: 32px;
    letter-spacing: -0.5px;
    color: var(--volt-yellow);
    white-space: nowrap;
  }

  /* Front side */
  .card-front { background: var(--card-white); color: var(--ink); }
  .card-front .ring-decor {
    position: absolute;
    left: -140px; top: 24px;
    width: 238px; height: 238px;
  }
  .card-front .brand-name {
    position: absolute;
    right: 32px; top: 38px;
    font-family: "Montserrat", Arial, sans-serif;
    font-weight: 800;
    font-size: 24px;
    letter-spacing: -0.4px;
    color: var(--ink);
    white-space: nowrap;
  }
  .card-front .person {
    position: absolute;
    left: 205px; top: 92px;
  }
  .person-name {
    font-family: "Montserrat", Arial, sans-serif;
    font-weight: 500;
    font-size: 24px;
    line-height: 1;
  }
  .person-title {
    font-weight: 700;
    font-size: 13px;
    margin-top: 3px;
  }
  .contact-list {
    list-style: none;
    position: absolute;
    left: 205px; top: 152px;
  }
  .contact-item {
    display: flex; align-items: center; gap: 11px;
    font-size: 14px;
    line-height: 20px;
    margin-bottom: 7px;
    white-space: nowrap;
  }
  .contact-icon {
    width: 20px; height: 20px;
    border-radius: 50%;
    background: var(--volt-yellow);
    display: flex; align-items: center; justify-content: center;
    flex-shrink: 0;
  }
  .contact-icon svg { width: 11px; height: 11px; fill: var(--ink); }
  .contact-icon svg.line-icon { fill: none; stroke: var(--ink); stroke-width: 2; }
</style>
</head>
<body>

  <section class="card card-back" aria-label="Card back">
    <div class="brand-mark">
      <div class="brand-circle"></div>
      <div class="brand-name">Volt Kettle Works</div>
    </div>
  </section>

  <section class="card card-front derek" aria-label="Card front, Derek Holm">
    <svg class="ring-decor" viewBox="0 0 250 250" aria-hidden="true">
      <circle cx="125" cy="125" r="113" fill="none" stroke="#151515" stroke-width="22"/>
    </svg>
    <div class="brand-name">Volt Kettle Works</div>
    <div class="person">
      <div class="person-name">Derek Holm</div>
      <div class="person-title">Owner</div>
    </div>
    <ul class="contact-list">
      <li class="contact-item">
        <span class="contact-icon"><svg viewBox="0 0 24 24"><path d="M6.6 10.8a15.1 15.1 0 0 0 6.6 6.6l2.2-2.2a1 1 0 0 1 1-.25 11.4 11.4 0 0 0 3.6.57 1 1 0 0 1 1 1V20a1 1 0 0 1-1 1A17 17 0 0 1 3 4a1 1 0 0 1 1-1h3.5a1 1 0 0 1 1 1c0 1.25.2 2.45.57 3.57a1 1 0 0 1-.25 1z"/></svg></span>
        888-472-0635
      </li>
      <li class="contact-item">
        <span class="contact-icon"><svg viewBox="0 0 24 24"><path d="M2 5h20v14H2zm2 2v.5l8 5 8-5V7l-8 5z"/></svg></span>
        derek@voltkettleworks.com
      </li>
      <li class="contact-item">
        <span class="contact-icon"><svg class="line-icon" viewBox="0 0 24 24"><circle cx="12" cy="12" r="9"/><path d="M3 12h18M12 3c3 3 3 15 0 18M12 3c-3 3-3 15 0 18"/></svg></span>
        voltkettleworks.com
      </li>
      <li class="contact-item">
        <span class="contact-icon"><svg viewBox="0 0 24 24"><path d="M12 2a7 7 0 0 0-7 7c0 5 7 13 7 13s7-8 7-13a7 7 0 0 0-7-7zm0 9.5A2.5 2.5 0 1 1 12 6.5a2.5 2.5 0 0 1 0 5z"/></svg></span>
        Lakeview, Texas 77512
      </li>
    </ul>
  </section>

  <section class="card card-front mona" aria-label="Card front, Mona Holm">
    <svg class="ring-decor" viewBox="0 0 250 250" aria-hidden="true">
      <circle cx="125" cy="125" r="113" fill="none" stroke="#151515" stroke-width="22"/>
    </svg>
    <div class="brand-name">Volt Kettle Works</div>
    <div class="person">
      <div class="person-name">Mona Holm</div>
      <div class="person-title">Owner</div>
    </div>
    <ul class="contact-list">
      <li class="contact-item">
        <span class="contact-icon"><svg viewBox="0 0 24 24"><path d="M6.6 10.8a15.1 15.1 0 0 0 6.6 6.6l2.2-2.2a1 1 0 0 1 1-.25 11.4 11.4 0 0 0 3.6.57 1 1 0 0 1 1 1V20a1 1 0 0 1-1 1A17 17 0 0 1 3 4a1 1 0 0 1 1-1h3.5a1 1 0 0 1 1 1c0 1.25.2 2.45.57 3.57a1 1 0 0 1-.25 1z"/></svg></span>
        888-472-0635
      </li>
      <li class="contact-item">
        <span class="contact-icon"><svg viewBox="0 0 24 24"><path d="M2 5h20v14H2zm2 2v.5l8 5 8-5V7l-8 5z"/></svg></span>
        mona@voltkettleworks.com
      </li>
      <li class="contact-item">
        <span class="contact-icon"><svg class="line-icon" viewBox="0 0 24 24"><circle cx="12" cy="12" r="9"/><path d="M3 12h18M12 3c3 3 3 15 0 18M12 3c-3 3-3 15 0 18"/></svg></span>
        voltkettleworks.com
      </li>
      <li class="contact-item">
        <span class="contact-icon"><svg viewBox="0 0 24 24"><path d="M12 2a7 7 0 0 0-7 7c0 5 7 13 7 13s7-8 7-13a7 7 0 0 0-7-7zm0 9.5A2.5 2.5 0 1 1 12 6.5a2.5 2.5 0 0 1 0 5z"/></svg></span>
        Lakeview, Texas 77512
      </li>
    </ul>
  </section>

</body>
</html>
```